High-End Medical Center Website Design Project

This design is part of a well thought-out project by an experienced project manager / developer. The approved wireframe is attached. Creative interpretations / suggestions based on the layout encouraged.

The design is for a new state-of-the-art medical center located in Dallas, Texas. The target audience would likely be individuals (approx. 60% female /40% male) who are the healthcare decision-makers for their families. They would likely have insurance and be inclined to seek out top-quality care.

Potential clients would choose this client over others in their industry because the medical center is physician owned, meaning it is patient-focused rather than profit-focused. The facility is brand new, featuring the latest technology. (This includes an amazing waiting room featuring WiFi and docking stations.) The physicians are hand-picked by referral only.

The look of the site should be extremely clean. We are going for a well-organized, professional look with a bit of a warm glow (interpret that however you like). Use crisp corners and the colors in the logo.

Think modern, clean with some great use of color / font.

We can get lovely photography of the medical center once construction is complete. Feel free to use an "example image" behind the Featured Area ("Physician Owned. Patient-Focused") if you like. We are open to ideas.

ONE CHANGE REQUESTED IN THE WIREFRAME:

Remove the "Connect" 1/4 page footer area and replace with a quick contact form. You may swap the "Locations" area with the form if desired. Put social media icons at the top left of the page in the top header area.

(Note: Please use social media icons that match the design rather than standard icons. We preferred not placing the icons at the top, but the client requested this. Let's not bring more attention to them than necessary.)
Updates

We're custom programming this site, so there's no need to base it on a template. Also, we would prefer not to use typical "seen everywhere" stock images.Thanks.

Industry/Entity Type

Construction

Requirements
Must have
• Follow the wireframe. This has been approved.
Nice to have
• Examples of what hover states, links or dropdowns might look like.

```html
<!DOCTYPE html>
<html lang="en">
<head>
<meta charset="utf-8">
<title>Nova Medical Center</title>
<link href="https://fonts.googleapis.com/css2?family=Montserrat:wght@500;600;700&family=Arimo:ital,wght@0,400;0,700;1,400&display=swap" rel="stylesheet">
<style>
:root{
  --blue:#0b5aa8;
  --teal:#43abba;
  --orange:#f0622f;
  --ink:#111;
  --grey:#5a5a5a;
  --nav:#444;
  --footer-bg:#dce8f3;
  --line:#e2e2e2;
}
*{box-sizing:border-box;margin:0;padding:0}
html,body{width:1145px;height:1200px;overflow:hidden}
body{position:relative;background:#fff;font-family:"Arimo",Arial,sans-serif;color:var(--ink)}
.abs{position:absolute}

/* header */
.top-stripe{left:0;top:0;width:1145px;height:4px;background:var(--teal)}
.phone-tab{left:872px;top:0;width:133px;height:24px;background:var(--teal);color:#fff;font-size:14px;display:flex;align-items:center;justify-content:center;gap:6px}
.header{left:0;top:4px;width:1145px;height:89px;border-bottom:1px solid var(--line)}
.brand{left:135px;top:29px;width:276px;height:39px;display:flex;align-items:center;gap:8px;font-family:"Montserrat",sans-serif;font-weight:700;font-size:17px;color:var(--blue);white-space:nowrap}
.brand-mark{flex:none;width:26px;height:26px;background:var(--blue)}
.main-nav{left:461px;top:52px;display:flex;gap:16px;font-family:"Montserrat",sans-serif;font-weight:700;font-size:13.5px;letter-spacing:.2px}
.main-nav a{color:var(--nav);text-decoration:none}
.main-nav a.active,.main-nav a:hover{color:var(--blue)}

/* hero */
.hero{left:53px;top:93px;width:1039px;height:380px;background:linear-gradient(100deg,#e8edf0 0%,#d7e2ea 30%,#eef1f3 55%,#c9d6e2 80%,#dfe6ec 100%)}
.hero-title{left:0;top:316px;width:1145px;text-align:center;font-family:"Montserrat",sans-serif;font-weight:700;font-size:30px;letter-spacing:-.8px;color:var(--blue)}
.service-circle{top:365px;width:76px;height:76px;border-radius:50%;border:4px solid #6b6b6b;background:#fff;display:flex;align-items:center;justify-content:center}
.slider-dots{left:978px;top:463px;display:flex;gap:2px}
.slider-dots span{width:7px;height:7px;border-radius:50%;background:#2a5a88}
.hero-rule{left:0;top:473px;width:1145px;height:2px;background:#e6e6e6}

/* features */
.intro-heading{left:135px;top:525px;font-family:"Montserrat",sans-serif;font-weight:700;font-size:19px;line-height:25px;color:var(--blue)}
.feature{top:527px;width:220px}
.feature h3{font-family:"Montserrat",sans-serif;font-weight:700;font-size:18px;color:var(--blue);margin-bottom:6px}
.feature p{font-size:12px;line-height:16px;color:var(--ink)}
.section-rule{left:0;top:634px;width:1145px;height:1px;background:var(--line)}

/* about */
.building-photo{left:136px;top:674px;width:262px;height:155px;background:linear-gradient(180deg,#b9cee0 0%,#9bb4c8 45%,#8a7a5f 75%,#c9c3b8 100%)}
.about-title,.testi-title{font-family:"Montserrat",sans-serif;font-weight:700;font-size:17px;color:var(--ink)}
.about-title{left:417px;top:679px}
.about-text{left:417px;top:710px;width:280px;font-size:13px;line-height:16px}
.btn{display:flex;align-items:center;justify-content:center;background:var(--orange);color:#fff;font-size:10px;letter-spacing:.3px;border:1px solid #d24d1f}
.btn-about{left:417px;top:816px;width:91px;height:19px}
.testi-title{left:771px;top:680px}
.avatar{left:774px;top:714px;width:37px;height:36px;background:linear-gradient(160deg,#c7d4df,#d8b59a 55%,#eae4de)}
.testi-name{left:825px;top:714px;font-size:12px;line-height:16px}
.testi-text{left:774px;top:760px;width:250px;font-size:12px;line-height:16px}
.btn-testi{left:771px;top:838px;width:90px;height:18px}
.quote-mark{left:975px;top:824px;font-family:Georgia,serif;font-size:48px;color:#b5b5b5;line-height:1}

/* footer */
.footer{left:0;top:890px;width:1145px;height:265px;background:var(--footer-bg)}
.col-title{display:flex;align-items:center;gap:8px;font-size:16.5px;color:var(--blue)}
.news-item{font-size:12px;line-height:14px;margin-bottom:10px}
.meta{font-size:10.5px;color:var(--grey)}
.meta i{font-style:italic}
.meta a{color:var(--ink);text-decoration:none;margin-left:4px}
.blog .meta a{color:var(--orange)}
.field{left:600px;width:177px;background:#fff;border:1px solid #c5ccd3;font-size:12px;color:#888;padding:5px 7px}
.btn-contact{left:600px;top:1088px;width:105px;height:24px;font-size:12px}
.wait-badge{left:819px;top:966px;width:51px;height:51px;border-radius:50%;background:var(--blue);color:#fff;font-size:19px;display:flex;align-items:center;justify-content:center}
.wait-text{left:879px;top:969px;width:84px;font-size:12px;line-height:17.5px}

/* bottom bar */
.bottom-bar{left:0;top:1155px;width:1145px;height:45px;background:var(--teal)}
.legal{left:159px;top:1170px;color:#fff;font-size:11px;white-space:nowrap}
.legal a{color:#fff;text-decoration:none}
.social{left:839px;top:1165px;display:flex;gap:8px}
.social span{width:25px;height:25px;border-radius:50%;border:1.5px solid #fff}
</style>
</head>
<body>

<div class="abs top-stripe"></div>
<div class="abs header"></div>
<div class="abs phone-tab">
  <svg width="11" height="11" viewBox="0 0 24 24" fill="#fff"><path d="M6.6 10.8a15 15 0 0 0 6.6 6.6l2.2-2.2c.3-.3.7-.4 1-.2 1.1.4 2.3.6 3.6.6.6 0 1 .4 1 1V20c0 .6-.4 1-1 1A17 17 0 0 1 3 4c0-.6.4-1 1-1h3.5c.6 0 1 .4 1 1 0 1.3.2 2.5.6 3.6.1.3 0 .7-.2 1z"/></svg>
  (555) 014 2290
</div>
<div class="abs brand"><span class="brand-mark"></span>NOVA MEDICAL CENTER</div>
<nav class="abs main-nav">
  <a href="#">WHY NOVA..</a>
  <a href="#" class="active">PHYCISIANS</a>
  <a href="#">SPECIALITIES</a>
  <a href="#">INFO</a>
  <a href="#">LOCATIONS</a>
  <a href="#">CONTACT</a>
</nav>

<div class="abs hero" role="img" aria-label="Photo of a smiling team of doctors and nurses in white coats and scrubs"></div>
<div class="abs hero-title">Physician Owned Patient Focused</div>
<div class="abs service-circle" style="left:457px">
  <svg width="30" height="36" viewBox="0 0 30 36" fill="none" stroke="#555" stroke-width="2.2" stroke-linecap="round"><path d="M7 3v9a6 6 0 0 0 12 0V3"/><path d="M13 18v6a6 6 0 0 0 12 0v-4"/><circle cx="25" cy="17" r="3"/></svg>
</div>
<div class="abs service-circle" style="left:552px">
  <svg width="34" height="30" viewBox="0 0 34 30" fill="#555"><path d="M12 4h10v4h-2V6h-6v2h-2z"/><rect x="2" y="8" width="30" height="20" rx="3"/><circle cx="17" cy="18" r="7" fill="#fff"/><path d="M15.5 14h3v2.5H21v3h-2.5V22h-3v-2.5H13v-3h2.5z"/></svg>
</div>
<div class="abs service-circle" style="left:648px">
  <svg width="36" height="30" viewBox="0 0 36 30" fill="#555"><rect x="3" y="3" width="3" height="24"/><rect x="30" y="8" width="3" height="19"/><path d="M6 14h24v6H6z"/><circle cx="12" cy="10" r="3.5"/><path d="M16 9h10l3 5H16z"/></svg>
</div>
<div class="abs slider-dots"><span></span><span></span><span></span></div>
<div class="abs hero-rule"></div>

<div class="abs intro-heading">lorem ipsum<br>dolor sit amet<br>consecte</div>
<div class="abs feature" style="left:300px">
  <h3>Technology</h3>
  <p>Lorem ipsum dolor sit amet, elit tempor incididunt ut labore et dolore magna aliqua ut enim ad minim...</p>
</div>
<div class="abs feature" style="left:552px">
  <h3>Quality of Care</h3>
  <p>Lorem ipsum dolor sit amet, elit tempor incididunt ut labore et dolore magna aliqua ut enim ad minim...</p>
</div>
<div class="abs feature" style="left:798px">
  <h3>Patient Experience</h3>
  <p>Lorem ipsum dolor sit amet, elit tempor incididunt ut labore et dolore magna aliqua ut enim ad minim...</p>
</div>
<div class="abs section-rule"></div>

<div class="abs building-photo" role="img" aria-label="Photo of the modern glass-fronted medical center building"></div>
<h2 class="abs about-title">What we do ?</h2>
<p class="abs about-text">Lorem ipsum dolor sit amet, consectetur adipisicing elit, sed do eiusmod tempor incididunt ut labore et dolore magna aliqua. Ut enim ad minim veniam, quis nostrud exercitation ullamco laboris nisi ut aliquip ex ea commodo consequat.</p>
<a class="abs btn btn-about">LEARN MORE</a>

<h2 class="abs testi-title">Testimonials</h2>
<div class="abs avatar" role="img" aria-label="Portrait photo of the surgeon"></div>
<div class="abs testi-name">Dr. Alan Reed<br>Sr. Surgen - USA</div>
<p class="abs testi-text">Lorem ipsum dolor sit amet, consectetur adipisicing elit, sed do eiusmod tempor incididunt ut labore et dolore magna aliqua. Ut enim ad minim veniam,</p>
<a class="abs btn btn-testi">LEARN MORE</a>
<div class="abs quote-mark">&#8221;</div>

<div class="abs footer"></div>

<section class="abs news" style="left:167px;top:925px">
  <div class="col-title" style="margin-bottom:16px">
    <svg width="15" height="18" viewBox="0 0 15 18" fill="none" stroke="#0b5aa8" stroke-width="1.6"><rect x="1" y="1" width="13" height="16"/><path d="M4 6h7M4 9h7M4 12h7"/></svg>News
  </div>
  <div class="news-item">Lorem ipsum dolor sit amet sed..<div class="meta"><i>22 July, 2013</i> &nbsp;| <a href="#">Read More</a></div></div>
  <div class="news-item">Lorem ipsum dolor sit amet sed..<div class="meta"><i>22 July, 2013</i> &nbsp;| <a href="#">Read More</a></div></div>
  <div class="news-item">Lorem ipsum dolor sit amet sed..<div class="meta"><i>22 July, 2013</i> &nbsp;| <a href="#">Read More</a></div></div>
</section>

<section class="abs blog" style="left:379px;top:925px">
  <div class="col-title" style="margin-bottom:14px">
    <svg width="21" height="14" viewBox="0 0 21 14" fill="#0b5aa8"><rect width="21" height="14" rx="1"/><circle cx="6" cy="6" r="2.2" fill="#fff"/><path d="M2.5 11.5a3.5 3 0 0 1 7 0z" fill="#fff"/><path d="M11 5h7v1.5h-7zM11 8h7v1.5h-7z" fill="#fff"/></svg>Blog
  </div>
  <div class="news-item" style="margin-bottom:16px">Consectetur adipisicing<br>Lorem ipsum dolor sit amet sed<div class="meta"><i>22 July, 2013</i> &nbsp;| <a href="#">Read More</a></div></div>
  <div class="news-item">Consectetur adipisicing<br>Lorem ipsum dolor sit amet sed<div class="meta"><i>22 July, 2013</i> &nbsp;| <a href="#">Read More</a></div></div>
</section>

<div class="abs col-title" style="left:596px;top:926px">
  <svg width="19" height="14" viewBox="0 0 19 14" fill="none" stroke="#0b5aa8" stroke-width="1.6"><rect x="1" y="1" width="17" height="12"/><path d="M1 1l8.5 7L18 1"/></svg>Quick Contact
</div>
<div class="abs field" style="top:962px;height:26px">Name</div>
<div class="abs field" style="top:992px;height:26px">Email</div>
<div class="abs field" style="top:1024px;height:55px">Comment</div>
<a class="abs btn btn-contact">CONTACT US</a>

<div class="abs col-title" style="left:817px;top:924px">
  <svg width="20" height="20" viewBox="0 0 20 20" fill="none" stroke="#0b5aa8" stroke-width="1.5"><circle cx="10" cy="10" r="8.5"/><path d="M10 4.5V10l3.5 2"/></svg>Average Wait Time
</div>
<div class="abs wait-badge">01</div>
<p class="abs wait-text">Consectetur adipisicing Lorem ipsum dolor sit amet sed adipisicing elit, sed do</p>

<div class="abs bottom-bar"></div>
<div class="abs legal">All Right Reserved &copy; Copyright with www.novamc.com &nbsp;- &nbsp;2013 &nbsp;&nbsp; <a href="#">Terms</a> &nbsp;. &nbsp;<a href="#">Privacy Policy</a></div>
<div class="abs social" aria-label="Social links"><span></span><span></span><span></span><span></span><span></span></div>

</body>
</html>
```